Cover Design for my E-Book

I'm looking for cover art for my new book project. It's a business book for musicians entering the field of music for advertising. While it's a business book, the tone of the book is casual, easy to understand and tongue in cheek and I am looking for a design that is simple, clean and modern. I would use the following book covers as references of styles that I think convey the right feeling:

Unwind
The Craft Of Routine
Nimble
Upturn by Dwight Calloway
Ethical Pluralism by Harold Brisket

While this direction is a general guide, I am open to being surprised by something very different from the above. I am a musician who worked with creative briefs all the time and I know how maddening they can be to read. I am only now learning how maddening they can be to write. thanks for your help.

Target Market(s)

Music business students, composers and bands

Industry/Entity Type

Business

Requirements
Must have
• Book Title:

Pitching UP - Thriving Across The Present Age Of Licensed Sound

My Name:

Gordon Tavaresco

```html
<!DOCTYPE html>
<html lang="en">
<head>
<meta charset="utf-8">
<title>Pitching Up — Gordon Tavaresco</title>
<link rel="stylesheet" href="https://fonts.googleapis.com/css2?family=Saira+Semi+Condensed:wght@700;800&family=Saira+Condensed:wght@700&family=Cinzel:wght@400;700&display=swap">
<style>
  :root {
    --page-bg: #ffffff;
    --cover-bg: #000000;
    --ink-light: #ffffff;
    --wood-warm: #8a4a2c;
    --wood-deep: #3a120c;
    --sound-hole: #c98a66;
  }
  html, body {
    margin: 0;
    padding: 0;
    width: 1000px;
    height: 1200px;
    overflow: hidden;
    background: var(--page-bg);
  }
  .canvas {
    position: relative;
    width: 1000px;
    height: 1200px;
  }
  .book-cover {
    position: absolute;
    left: 157px;
    top: 58px;
    width: 712px;
    height: 1070px;
    background: var(--cover-bg);
    overflow: hidden;
  }
  .cover-art {
    position: absolute;
    left: 0;
    top: 330px;
    width: 712px;
    height: 660px;
    background:
      radial-gradient(ellipse 34% 12% at 50% 38%, var(--sound-hole) 0%, rgba(201,138,102,0.4) 45%, rgba(0,0,0,0) 100%),
      radial-gradient(ellipse 60% 45% at 50% 55%, var(--wood-warm) 0%, var(--wood-deep) 45%, var(--cover-bg) 85%);
  }
  .cover-type {
    position: absolute;
    inset: 0;
  }
  .title {
    font-family: "Saira Semi Condensed", "Arial Narrow", sans-serif;
    font-weight: 800;
    fill: var(--ink-light);
  }
  .subtitle {
    font-family: "Saira Condensed", "Arial Narrow", sans-serif;
    font-weight: 700;
    fill: var(--ink-light);
  }
  .author {
    position: absolute;
    left: 0;
    right: 0;
    top: 990px;
    margin: 0;
    text-align: center;
    font-family: "Cinzel", "Times New Roman", serif;
    font-weight: 400;
    font-size: 56px;
    letter-spacing: 2px;
    color: var(--ink-light);
  }
</style>
</head>
<body>
<div class="canvas">
  <div class="book-cover">
    <div class="cover-art" role="img" aria-label="Close-up photograph of an acoustic guitar, looking down the strings over the sound hole toward the bridge pins, on a dark background"></div>
    <svg class="cover-type" width="712" height="1070" viewBox="0 0 712 1070" aria-label="Pitching Up: Thriving Across the Present Age of Licensed Sound">
      <text class="title" x="35" y="177" font-size="200" textLength="630" lengthAdjust="spacingAndGlyphs">PITCHING UP</text>
      <text class="subtitle" x="36" y="252" font-size="52" textLength="633" lengthAdjust="spacingAndGlyphs">THRIVING ACROSS THE PRESENT AGE</text>
      <text class="subtitle" x="131" y="302" font-size="52" textLength="457" lengthAdjust="spacingAndGlyphs">OF LICENSED SOUND</text>
    </svg>
    <p class="author">Gordon Tavaresco</p>
  </div>
</div>
</body>
</html>
```